Mortgage Loan officer needs clean/modern business card design

Looking for a clean, modern 2-sided business card design. We like the earth tones used in our logo and website http://vukarhome-lending.example . Would also like to incorporate: 1) Something special to make our card stand out - a pop of color or embossed logo, for instance and 2) please include "Mortgage Loans" "Reverse Mortgages" "Private Money Loans" on back of card with the logo.

Front: Needs to include agent/company license info - see website. Agent name: Niall Hargrove

Here are fonts and colors used for our logo:
Font: Avenir Next
Colors:
#2c3539 - Dark Gray
#576870 - Light Gray
#ffffff - Background White

Target Market(s)

Prospects and current clients. Will also be distributing to people in professional network (attorneys and CPAs)

Industry/Entity Type

Business

Contact Information for Business Card

Include agent name, contact info, website on front, licensing info for agent an company. Logo and services offered on back

Font styles to use
Other font styles liked:
• Avenir Next

Requirements
Must have
• See project description
Should not have
• Nothing cheesy

```html
<!DOCTYPE html>
<html lang="en">
<head>
<meta charset="utf-8">
<title>Niall Hargrove – Business Card</title>
<link href="https://fonts.googleapis.com/css2?family=Nunito+Sans:wght@400;600;800&display=swap" rel="stylesheet">
<style>
  :root {
    --dark-gray: #2c3539;
    --light-gray: #576870;
    --white: #ffffff;
    --black: #0b0b0b;
    --rule: #b9c0c3;
    --stage: #e9eaea;
  }
  * { box-sizing: border-box; margin: 0; padding: 0; }
  html, body { width: 960px; height: 1200px; overflow: hidden; }
  body {
    background: var(--stage);
    font-family: "Nunito Sans", "Avenir Next", sans-serif;
    position: relative;
  }
  .card {
    position: absolute;
    left: 100px;
    width: 760px;
    height: 434px;
    box-shadow: 0 10px 30px rgba(0,0,0,0.12);
  }
  .card--front { top: 110px; background: var(--white); color: var(--dark-gray); }
  .card--back { top: 650px; background: var(--black); color: var(--white); }

  /* Front */
  .identity { position: absolute; left: 52px; top: 118px; }
  .identity__name {
    font-size: 44px; font-weight: 800; letter-spacing: 0.5px;
    text-transform: uppercase; line-height: 1;
  }
  .identity__surname { color: var(--light-gray); }
  .identity__row { display: flex; gap: 44px; margin-top: 8px; align-items: baseline; }
  .identity__title { font-size: 24px; color: var(--dark-gray); }
  .identity__mobile { font-size: 22px; color: var(--dark-gray); letter-spacing: 1px; }
  .divider {
    position: absolute; left: 30px; right: 30px; top: 238px;
    height: 1px; background: var(--rule);
  }
  .license {
    position: absolute; right: 40px; top: 250px;
    text-align: right; font-size: 17px; line-height: 1.35; color: var(--dark-gray);
  }
  .contacts { position: absolute; left: 40px; bottom: 40px; list-style: none; }
  .contacts li {
    display: flex; align-items: center; gap: 8px;
    font-size: 17px; line-height: 1.55; color: var(--dark-gray);
  }
  .contacts svg { width: 17px; height: 17px; flex: none; }

  /* Back */
  .brand-seal {
    position: absolute; left: 80px; top: 110px;
    width: 214px; height: 214px; border-radius: 50%;
    background: var(--white);
    display: flex; align-items: center; justify-content: center; text-align: center;
  }
  .brand-seal__name {
    font-size: 24px; font-weight: 400; line-height: 1.25; color: var(--light-gray);
  }
  .back-divider {
    position: absolute; left: 360px; top: 110px;
    width: 1px; height: 180px; background: #8a8a8a;
  }
  .services {
    position: absolute; left: 410px; top: 140px; list-style: none;
    font-size: 22px; font-weight: 600; letter-spacing: 0.6px;
    text-transform: uppercase; line-height: 1.75;
  }
</style>
</head>
<body>
  <section class="card card--front" aria-label="Card front">
    <div class="identity">
      <h1 class="identity__name">Niall <span class="identity__surname">Hargrove</span></h1>
      <div class="identity__row">
        <span class="identity__title">Loan Officer</span>
        <span class="identity__mobile">+ 555 - 210 - 4471</span>
      </div>
    </div>
    <div class="divider"></div>
    <p class="license">
      Fed and State License<br>
      NMLS:410527 DRE:02846173<br>
      CO: DRE:02250961/NMLS:507382
    </p>
    <ul class="contacts">
      <li>
        <svg viewBox="0 0 20 20" aria-hidden="true"><circle cx="10" cy="10" r="10" fill="var(--dark-gray)"/><path d="M6 8c0-1.5 1.8-2.2 4-2.2s4 .7 4 2.2l-1.5.5-.5-1.2H8l-.5 1.2z M7.5 10h5l1 4h-7z" fill="#fff"/></svg>
        + 555-318-6020 x 214
      </li>
      <li>
        <svg viewBox="0 0 20 20" aria-hidden="true"><circle cx="10" cy="10" r="10" fill="var(--dark-gray)"/><rect x="6" y="5" width="8" height="4" fill="#fff"/><rect x="5" y="9.5" width="10" height="5.5" rx="1" fill="#fff"/><rect x="7" y="11" width="6" height="1" fill="var(--dark-gray)"/></svg>
        + 555 - 318 - 7392
      </li>
      <li>
        <svg viewBox="0 0 20 20" aria-hidden="true"><circle cx="10" cy="10" r="10" fill="var(--dark-gray)"/><g fill="none" stroke="#fff" stroke-width="1.1"><circle cx="10" cy="10" r="5"/><ellipse cx="10" cy="10" rx="2.2" ry="5"/><line x1="5" y1="10" x2="15" y2="10"/></g></svg>
        www.vukarhome-lending.example
      </li>
    </ul>
  </section>

  <section class="card card--back" aria-label="Card back">
    <div class="brand-seal">
      <span class="brand-seal__name">The Hargrove<br>Group</span>
    </div>
    <div class="back-divider"></div>
    <ul class="services">
      <li>Mortgage Loans</li>
      <li>Reverse Mortgages</li>
      <li>Private Money Loans</li>
    </ul>
  </section>
</body>
</html>
```